Global Marketing company needs a new look!

Please see attached brief for a new design of our website and other materials. This will include icons, appearance, structure etc. We are a global, leading marketing agency with a passion for innovation and giving our clients the best ROI possible. Please make it elegant as we want to attract high end customers- some of our clients include Stremora, BQ autos and Petalwick so these are the preminum clients we are aiming for and so we don't want it to look cheap or tacky.

Industry/Entity Type

It Company

Number of Pages Required

1 page

Colors
ffc214
ffffff
474747

Requirements
Nice to have
• Icons to represent sales, increases etc

```html
<!DOCTYPE html>
<html lang="en">
<head>
<meta charset="utf-8">
<title>Vantera — Digital Performance Re-Invented</title>
<link rel="stylesheet" href="https://fonts.googleapis.com/css2?family=Oswald:wght@300;400&family=Exo+2:wght@400;500&family=Crimson+Pro:wght@600&family=Roboto:wght@400&display=swap">
<style>
  :root {
    --yellow: #ffc214;
    --white: #ffffff;
    --charcoal: #474747;
    --ink: #2f2f2f;
    --nav: #5b5a5c;
    --paper: #f4f4f4;
    --teal: #8ec3c1;
    --body: #3a3a3a;
  }
  * { box-sizing: border-box; margin: 0; padding: 0; }
  html, body { width: 1200px; height: 2327px; overflow: hidden; background: var(--white); }
  body { position: relative; font-family: "Roboto", sans-serif; color: var(--body); }

  .cookie-bar {
    position: absolute; top: 0; left: 0; width: 1200px; height: 41px;
    background: var(--yellow); display: flex; align-items: center; justify-content: center;
    gap: 14px; font-size: 12px; color: #222;
  }
  .cookie-bar .accept { background: #111; color: var(--white); padding: 4px 8px; font-weight: 700; }
  .cookie-bar .read-more { color: #6b5300; text-decoration: underline; }

  .hero {
    position: absolute; top: 41px; left: 0; width: 1200px; height: 802px;
    background: linear-gradient(180deg, #2a2622 0%, #4b4640 35%, #3c3935 70%, #2b2a29 100%);
  }
  .hero-brand { position: absolute; left: 240px; top: 195px; width: 303px; text-align: center; }
  .brand-rule { display: flex; align-items: center; justify-content: center; gap: 18px; }
  .brand-rule span.line { width: 70px; height: 2px; background: var(--white); }
  .brand-name { font-family: "Exo 2", sans-serif; font-weight: 500; font-size: 30px; color: var(--white); display: flex; align-items: center; gap: 8px; }
  .brand-name .dot { width: 12px; height: 12px; border-radius: 50%; background: var(--white); }
  .headline { font-family: "Oswald", sans-serif; font-weight: 300; color: var(--white); text-transform: uppercase; line-height: 1; }
  .headline .big { display: block; font-size: 118px; margin-top: 18px; letter-spacing: 1px; }
  .headline .mid { display: block; font-size: 58px; margin-top: 6px; }
  .headline .end { display: block; font-size: 70px; margin-top: 6px; }
  .hero-rule { width: 303px; height: 2px; background: var(--white); margin: 18px 0 16px; }
  .services-list { font-family: "Exo 2", sans-serif; font-size: 24px; color: var(--yellow); line-height: 32px; text-align: left; letter-spacing: 0.5px; }

  .video-player { position: absolute; left: 664px; top: 348px; width: 367px; height: 227px; background: #111; padding: 10px 0; }
  .video-frame { width: 100%; height: 100%; background: linear-gradient(90deg, #f2b92a 0 35%, #9fb9bd 35% 100%); position: relative; }
  .video-controls { position: absolute; left: 8px; right: 8px; bottom: 8px; height: 30px; display: flex; align-items: center; gap: 8px; }
  .play-btn { width: 46px; height: 30px; background: rgba(20,20,20,.85); display: flex; align-items: center; justify-content: center; }
  .scrub { flex: 1; height: 8px; background: rgba(20,20,20,.7); }
  .player-name { font-family: "Exo 2", sans-serif; font-size: 14px; color: var(--white); background: rgba(20,20,20,.85); padding: 4px 8px; }

  .site-nav { position: absolute; top: 843px; left: 0; width: 1200px; height: 86px; background: var(--nav); }
  .site-nav .brand-name { position: absolute; left: 162px; top: 24px; }
  .nav-links { position: absolute; left: 397px; top: 0; height: 86px; display: flex; align-items: center; gap: 24px; list-style: none; font-family: "Exo 2", sans-serif; font-size: 14px; color: var(--white); }
  .nav-links .caret::after { content: ""; display: inline-block; margin-left: 6px; border: 5px solid transparent; border-top-color: var(--white); border-bottom: 0; vertical-align: middle; }
  .nav-phone { position: absolute; left: 922px; top: 0; line-height: 86px; font-family: "Exo 2", sans-serif; font-size: 14px; color: var(--yellow); }

  .section-title { font-family: "Crimson Pro", serif; font-weight: 600; font-size: 35px; line-height: 36px; text-transform: uppercase; text-align: center; letter-spacing: 0.5px; }
  .title-rule { width: 136px; height: 3px; margin: 14px auto 0; }
  .section-copy { font-size: 15px; line-height: 26px; text-align: center; }

  .network { position: absolute; top: 929px; left: 0; width: 1200px; height: 542px; background: var(--paper); }
  .network .section-title { margin-top: 34px; color: var(--charcoal); }
  .network .title-rule { background: var(--charcoal); }
  .network .section-copy { margin-top: 20px; color: var(--body); }
  .devices-art { position: absolute; left: 263px; top: 252px; width: 687px; height: 232px; background: linear-gradient(180deg, #9ccac6, #7fb6b3); border-radius: 6px; }

  .talent { position: absolute; top: 1471px; left: 0; width: 1200px; height: 332px; background: linear-gradient(180deg, #3e3e3e, #262626 60%, #333); }
  .talent .notch { position: absolute; top: 0; left: 503px; }
  .talent .section-title { color: var(--yellow); margin-top: 104px; }
  .talent .title-rule { background: var(--yellow); }
  .talent .section-copy { color: var(--white); margin-top: 40px; line-height: 21px; }

  .results { position: absolute; top: 1803px; left: 0; width: 1200px; height: 487px; background: var(--paper); }
  .results .pointer { position: absolute; top: 0; left: 503px; }
  .results .section-title { color: var(--charcoal); margin-top: 86px; }
  .results .title-rule { background: var(--charcoal); }
  .result-item { position: absolute; top: 224px; width: 220px; margin-left: -110px; text-align: center; }
  .result-item svg { display: block; margin: 0 auto; }
  .result-item p { margin-top: 18px; font-size: 15px; line-height: 21px; color: var(--body); }
</style>
</head>
<body>

<div class="cookie-bar">
  <span>This website uses cookies to improve your experience. We'll assume you're ok with this, but you can opt-out if you wish.</span>
  <span class="accept">Accept</span>
  <span class="read-more">Read More</span>
</div>

<header class="hero" role="img" aria-label="City skyline of glass towers under a cloudy evening sky with a faint network of connected nodes">
  <div class="hero-brand">
    <div class="brand-rule"><span class="line"></span><span class="brand-name"><span class="dot"></span>Vantera</span><span class="line"></span></div>
    <h1 class="headline"><span class="big">Digital</span><span class="mid">Performance</span><span class="end">Re-Invented</span></h1>
    <div class="hero-rule"></div>
    <div class="services-list">PPC - DISPLAY - PAID SOCIAL<br>SEO - CONTENT - ANALYTICS</div>
  </div>

  <div class="video-player">
    <div class="video-frame" role="img" aria-label="Video still of a company spokesperson introducing the agency">
      <div class="video-controls">
        <span class="play-btn"><svg width="14" height="16" viewBox="0 0 14 16"><path d="M0 0L14 8L0 16Z" fill="#fff"/></svg></span>
        <span class="scrub"></span>
        <span class="player-name">HD Playbox</span>
      </div>
    </div>
  </div>
</header>

<nav class="site-nav">
  <span class="brand-name"><span class="dot"></span>Vantera</span>
  <ul class="nav-links">
    <li class="caret">SERVICES</li><li>TEAM</li><li>TECH</li><li>BLOG</li><li class="caret">JOIN US</li><li>CONTACT</li>
  </ul>
  <span class="nav-phone">UK: +44 20 5550 0142</span>
</nav>

<section class="network">
  <h2 class="section-title">First- we have the only worldwide<br>network of digital specialist</h2>
  <div class="title-rule"></div>
  <p class="section-copy">With over 600 specialists in 75 countries speaking 80 languages – we deliver global and local<br>cross-channel campaigns. Because there is never a substitute for truly local expertise</p>
  <div class="devices-art" role="img" aria-label="Illustration of a tablet, laptop and phone showing a world map with location markers"></div>
</section>

<section class="talent" role="img" aria-label="Black and white photo of the team working at desks in an open-plan office">
  <svg class="notch" width="223" height="32" viewBox="0 0 223 32"><path d="M0 0H223L111.5 32Z" fill="#f4f4f4"/></svg>
  <h2 class="section-title">Second – we recruit and retain the<br>finest in-house talent</h2>
  <div class="title-rule"></div>
  <p class="section-copy">Everyone in the team is a shareholder – so when you win we win – giving us a staff retention of<br>96% and unrivalled account management continuity</p>
</section>

<section class="results">
  <svg class="pointer" width="223" height="34" viewBox="0 0 223 34"><path d="M0 0H223L111.5 34Z" fill="#2b2b2b"/></svg>
  <h2 class="section-title">The result 5 years later?</h2>
  <div class="title-rule"></div>

  <div class="result-item" style="left:231px">
    <svg width="110" height="100" viewBox="0 0 110 100" fill="var(--teal)">
      <rect x="10" y="55" width="16" height="35"/><rect x="32" y="42" width="16" height="48"/><rect x="54" y="50" width="16" height="40"/><rect x="76" y="30" width="16" height="60"/>
      <path d="M6 50L40 22L60 38L92 10" stroke="var(--teal)" stroke-width="7" fill="none"/><path d="M80 4H100V24Z"/>
      <circle cx="44" cy="76" r="20" fill="#fff" stroke="var(--teal)" stroke-width="5"/>
    </svg>
    <p>Searchline's Fastest Growing<br>Agency</p>
  </div>

  <div class="result-item" style="left:495px">
    <svg width="100" height="100" viewBox="0 0 100 100">
      <rect x="14" y="20" width="70" height="72" fill="var(--teal)"/><path d="M14 92L60 46L84 70V92Z" fill="#6fa9a6"/>
      <path d="M66 6a18 18 0 0 1 18 18c0 14-18 32-18 32s-18-18-18-32a18 18 0 0 1 18-18z" fill="var(--teal)" stroke="#fff" stroke-width="3"/><circle cx="66" cy="24" r="6" fill="#fff"/>
    </svg>
    <p>Hubs in London, New York,<br>Sydney and Singapore</p>
  </div>

  <div class="result-item" style="left:726px">
    <svg width="90" height="100" viewBox="0 0 90 100" fill="var(--teal)">
      <circle cx="45" cy="26" r="20"/><path d="M5 98C5 70 22 54 45 54S85 70 85 98Z"/><circle cx="45" cy="80" r="10" fill="#fff"/><circle cx="45" cy="80" r="4"/>
    </svg>
    <p>Over 600 experts in every<br>digital discipline</p>
  </div>

  <div class="result-item" style="left:974px">
    <svg width="100" height="100" viewBox="0 0 100 100">
      <circle cx="50" cy="32" r="24" fill="var(--teal)"/><text x="50" y="42" text-anchor="middle" font-family="Roboto, sans-serif" font-size="28" fill="#fff">$</text>
      <path d="M6 66H30L46 74H66C72 74 72 82 66 82H46M66 80L88 68C94 66 97 72 92 76L62 94H30L6 86" fill="none" stroke="var(--teal)" stroke-width="5" stroke-linejoin="round"/>
    </svg>
    <p>Reputation for treating<br>clients' money like it's our</p>
  </div>
</section>

</body>
</html>
```